Law firm Seeks Modern and Engaging Site Redesign

Law firm seeks a new web site. Should be modern, but retaining existing logo. Needs to include contact section, professional bio, services offered, and contact information.

The site should be modern, responsive, and able to be SEO optimized.

The finished product should be coded in a Wordpress site, which I will provide. I can work with other platforms, including Wix, but WP is preferred.

Note the current site is https://www.tallowfinchlaw.com/#/home

Target Market(s)

Family Law Practice

Industry/Entity Type

Legal

Coding

Coded - Design and coding required

Number of Pages Required

4 page

Font styles to use
Sans Serif

Requirements
Must have
• Service description
Bio pages for partners
Contact Form
Awards/Publication page

```html
<!DOCTYPE html>
<html lang="en">
<head>
<meta charset="utf-8">
<title>Tallow | Finch — Attorneys at Law</title>
<link href="https://fonts.googleapis.com/css2?family=Roboto:wght@400;500;700;900&family=Raleway:wght@400;500;600&display=swap" rel="stylesheet">
<style>
:root{
  --ink:#1d1d1f;
  --dark:#1a1a1a;
  --blue:#4a78e0;
  --navy:#1b2f6e;
  --muted:#5d5f66;
  --band:#eef0f5;
  --white:#ffffff;
  --line:#d6d9e0;
}
*{box-sizing:border-box;margin:0;padding:0}
html,body{width:1200px;height:3634px;overflow:hidden;background:var(--white)}
body{font-family:"Raleway",sans-serif;color:var(--ink);position:relative}
.abs{position:absolute}
.btn{position:absolute;background:var(--blue);color:var(--white);font:500 12px "Raleway",sans-serif;text-transform:uppercase;display:flex;align-items:center;justify-content:center;letter-spacing:.2px}
.photo{position:absolute}

/* header + hero */
.hero{left:0;top:0;width:1200px;height:547px;background:linear-gradient(135deg,#262628 0%,#161617 100%)}
.topbar{left:0;top:0;width:1200px;height:28px;background:#111112}
.social{display:flex;gap:12px}
.social span{width:12px;height:12px;background:var(--white);border-radius:2px;display:block}
.topbar .social{position:absolute;left:93px;top:8px}
.topbar .contact{position:absolute;right:93px;top:7px;color:var(--white);font:500 11px "Raleway",sans-serif}
.brand{position:absolute;left:93px;top:40px;display:flex;align-items:center;gap:8px;font:400 21px "Raleway",sans-serif;color:var(--white)}
.brand .bar{width:3px;height:30px;background:var(--blue)}
.brand small{position:absolute;left:91px;top:26px;font-size:7px;color:var(--blue);white-space:nowrap}
.nav{position:absolute;top:50px;right:93px;display:flex;gap:40px;font:500 12px "Raleway",sans-serif;color:var(--white)}
.nav .on{color:var(--blue)}
.hero-kicker{left:92px;top:168px;font:400 25px "Raleway",sans-serif;color:var(--white)}
.hero-title{left:90px;top:192px;font:700 68px "Roboto",sans-serif;color:var(--white);letter-spacing:-.5px;white-space:nowrap}
.hero-title .sep{color:var(--blue);font-weight:400}
.hero-title .blue{color:var(--blue)}
.hero-text{left:93px;top:275px;width:400px;font:500 13.5px/21px "Raleway",sans-serif;color:var(--white)}

/* section headings */
.h-section{position:absolute;width:1200px;left:0;text-align:center;font:900 48px "Roboto",sans-serif;color:var(--ink);letter-spacing:-.3px}
.body-text{font:400 13px/21px "Raleway",sans-serif;color:var(--muted)}

/* who */
.who-h{left:526px;top:652px;font:900 48px "Roboto",sans-serif}
.who-text{left:526px;top:723px;width:575px}
.who-text p{margin-bottom:10px}

/* services */
.band{left:0;top:1022px;width:1107px;height:614px;background:var(--band)}
.svc-h{position:absolute;font:500 30px "Roboto",sans-serif;color:var(--ink)}
.svc-lead{position:absolute;width:540px}
.accepts{position:absolute;font:600 12px "Raleway",sans-serif;color:var(--ink)}
.items{position:absolute;display:grid;grid-template-columns:272px 272px;row-gap:8px}
.item{display:flex;align-items:center;gap:9px;font:500 11px "Raleway",sans-serif;color:var(--ink);height:46px;white-space:nowrap}
.item i{width:45px;height:45px;border-radius:50%;background:var(--blue);flex:none;display:flex;align-items:center;justify-content:center}
.item i::after{content:"";width:17px;height:17px;border:2.5px solid var(--white);border-radius:50%}

/* partners */
.card{position:absolute;top:2256px;width:324px}
.card .photo{position:relative;width:324px;height:337px}
.card h3{margin-top:27px;font:500 23px "Roboto",sans-serif;color:var(--ink)}
.card p{margin-top:10px;height:90px;font:400 12.5px/21px "Raleway",sans-serif;color:var(--muted)}
.card .btn{position:relative;width:106px;height:35px}
.arrow{position:absolute;top:2397px;width:54px;height:54px;border-radius:50%;background:var(--blue);display:flex;align-items:center;justify-content:center}

/* quick contact */
.qc{left:93px;top:2843px;width:1107px;height:397px;background:linear-gradient(90deg,#3a66d6 0%,#4a78e0 60%,#4f7fe6 100%)}
.qc-h{left:599px;top:2892px;font:900 50px "Roboto",sans-serif;color:var(--white)}
.qc-sub{left:599px;top:2947px;font:400 13.5px "Raleway",sans-serif;color:var(--white)}
.field{position:absolute;background:var(--white);border:1px solid var(--line);font:400 11px "Raleway",sans-serif;color:#444;padding:10px 10px}
.submit{position:absolute;left:857px;top:3152px;width:250px;height:32px;background:var(--navy);color:var(--white);font:500 11px "Raleway",sans-serif;display:flex;align-items:center;justify-content:center}

/* footer */
.footer{left:0;top:3240px;width:1200px;height:394px;background:linear-gradient(180deg,#1c1c1d,#121213)}
.f-h{position:absolute;top:3301px;font:500 21px "Roboto",sans-serif;color:var(--white)}
.f-list{position:absolute;top:3346px;list-style:none;font:400 12px "Raleway",sans-serif;color:var(--white)}
.f-list li{height:28.5px;display:flex;align-items:flex-start;gap:6px}
.f-list li .dot{width:9px;height:9px;border:2px solid var(--blue);border-radius:50%;margin-top:3px;flex:none}
.f-contact{position:absolute;left:441px;top:3346px;font:400 12px/16px "Raleway",sans-serif;color:var(--white)}
.f-contact div{display:flex;gap:8px;margin-bottom:15px}
.f-contact svg{flex:none;margin-top:2px}
.f-social{position:absolute;left:564px;top:3529px}
.copy{position:absolute;top:3557px;width:1200px;text-align:center;font:400 12px "Raleway",sans-serif;color:#9a9ba0}
.copy b{color:var(--white);font-weight:500}
</style>
</head>
<body>

<div class="abs hero"></div>
<div class="abs topbar">
  <div class="social"><span></span><span></span><span></span></div>
  <div class="contact">Contact Us: (555) 742-6093</div>
</div>
<div class="brand">Tallow<span class="bar"></span>Finch<small>Attorneys at Law</small></div>
<nav class="nav"><span class="on">Home</span><span>Family Law</span><span>Criminal Law</span><span>About</span><span>Contact</span></nav>

<div class="photo" role="img" aria-label="Portrait of the two founding partners in dark suits" style="left:563px;top:85px;width:544px;height:514px;background:linear-gradient(160deg,#2f56c9 0%,#1d3fa6 60%,#16308a 100%)"></div>

<div class="abs hero-kicker">The Law Firm of</div>
<div class="abs hero-title">Tallow <span class="sep">|</span> <span class="blue">Finch</span></div>
<p class="abs hero-text">LLC is based in Alder County, conveniently located in Harborview, New Jersey in 40 Meridian Plaza.</p>
<div class="btn" style="left:93px;top:336px;width:116px;height:36px">Get in touch</div>

<div class="photo" role="img" aria-label="Hands signing a legal document beside a laptop" style="left:93px;top:664px;width:395px;height:295px;border-radius:0 34px 0 34px;background:linear-gradient(135deg,#2a3f66 0%,#4d6a99 50%,#1c2a44 100%)"></div>
<h2 class="abs who-h">WHO WE ARE</h2>
<div class="abs who-text body-text">
  <p>The law firm of Tallow Finch, LLC is based in Alder County, conveniently located in Harborview, New Jersey in 40 Meridian Plaza. We serve the needs of clients throughout Alder County, as well as, clients from several other counties, including, but not limited to, Pine, Morrow, Easton and Hollis. Between our partners, we have over 30+ years of experience assisting clients with all of their family law and criminal law needs.</p>
  <p>Often times the areas of family law and criminal law cross paths, which can be both emotionally and financially complex. We understand that our client's case is unique and pride ourselves on being responsive to all of our clients needs.</p>
</div>
<div class="btn" style="left:526px;top:924px;width:104px;height:35px">About us</div>

<div class="abs band"></div>
<h2 class="h-section" style="top:1077px">OUR SERVICES</h2>

<h3 class="svc-h" style="left:93px;top:1158px">Family Law</h3>
<p class="svc-lead body-text" style="left:93px;top:1205px">Our legal team brings more than 30+ years of experience to assist in all of your family law needs. Call (555) 742-6093 to schedule an initial consultation.</p>
<div class="accepts" style="left:93px;top:1270px">Our firm accepts all kinds of family law matters, including:</div>
<div class="items" style="left:93px;top:1313px">
  <div class="item"><i></i>Divorce</div>
  <div class="item"><i></i>Pre-nuptial agreements</div>
  <div class="item"><i></i>Child Custody</div>
  <div class="item"><i></i>High-net worth and complex divorce cases</div>
  <div class="item"><i></i>Child Support</div>
  <div class="item"><i></i>Domestic violence</div>
</div>
<div class="btn" style="left:93px;top:1495px;width:106px;height:35px">Read more</div>
<div class="photo" role="img" aria-label="Lawyer and clients reviewing a divorce policy book at a desk" style="left:675px;top:1165px;width:432px;height:406px;background:linear-gradient(170deg,#3a3f47 0%,#2a2e35 45%,#1b1e24 100%)"></div>

<div class="photo" role="img" aria-label="Judge's gavel beside hands reviewing papers" style="left:93px;top:1702px;width:433px;height:406px;background:linear-gradient(135deg,#3b3a36 0%,#5c564c 45%,#1f1e1c 100%)"></div>
<h3 class="svc-h" style="left:558px;top:1695px">Criminal Law</h3>
<p class="svc-lead body-text" style="left:558px;top:1743px">Our legal team brings more than 30+ years of experience to assist in all of your family law needs. Call (555) 742-6093 to schedule an initial consultation.</p>
<div class="accepts" style="left:558px;top:1806px">Our firm accepts all kinds of family law matters, including:</div>
<div class="items" style="left:558px;top:1847px">
  <div class="item"><i></i>Assault</div>
  <div class="item"><i></i>Sex Crimes</div>
  <div class="item"><i></i>Domestic Violence</div>
  <div class="item"><i></i>Theft/Fraud Crimes</div>
  <div class="item"><i></i>Drug Crimes</div>
  <div class="item"><i></i>Expungements</div>
</div>
<div class="btn" style="left:558px;top:2032px;width:106px;height:35px">Read more</div>

<h2 class="h-section" style="top:2162px">OUR PARTNER</h2>
<div class="arrow" style="left:20px"><svg width="16" height="16" viewBox="0 0 16 16"><path d="M10 3 5 8l5 5" fill="none" stroke="#fff" stroke-width="2"/></svg></div>
<div class="arrow" style="left:1126px"><svg width="16" height="16" viewBox="0 0 16 16"><path d="M6 3l5 5-5 5" fill="none" stroke="#fff" stroke-width="2"/></svg></div>

<div class="card" style="left:93px">
  <div class="photo" role="img" aria-label="Portrait of partner Daniel R. Tallow in an office" style="background:linear-gradient(180deg,#d9d6cf 0%,#a8a59d 50%,#2a3550 100%)"></div>
  <h3>Daniel R. Tallow</h3>
  <p>Daniel R. Tallow practices in the area of family law, specializing in high conflict matters relating to divorce, custody, equitable distribution, and complex financial issues.</p>
  <div class="btn">Read more</div>
</div>
<div class="card" style="left:437px">
  <div class="photo" role="img" aria-label="Portrait of partner Marcus J. Finch seated at a desk" style="background:linear-gradient(180deg,#7a6a58 0%,#4a3f34 50%,#1d2233 100%)"></div>
  <h3>Marcus J. Finch</h3>
  <p>Marcus J. Finch is one of the founding partners of the firm. Mr. Finch's primary concentration is in the areas of matrimonial, family law, appellate work, juvenile...</p>
  <div class="btn">Read more</div>
</div>
<div class="card" style="left:781px">
  <div class="photo" role="img" aria-label="Portrait of associate Laura M. Castell outdoors" style="background:linear-gradient(180deg,#b9a89a 0%,#8e8a86 50%,#2a2a2e 100%)"></div>
  <h3>Laura M. Castell</h3>
  <p>Laura M. Castell has been an associate at Tallow Finch since 2016. In private practice, Ms. Castell focuses her practice on family and divorce law, which includes child custody, child and spousal support,,</p>
  <div class="btn">Read more</div>
</div>

<div class="abs qc"></div>
<div class="photo" role="img" aria-label="Partner standing in a dark suit" style="left:233px;top:2824px;width:239px;height:416px;background:linear-gradient(180deg,rgba(30,40,70,0) 0%,#1f2b52 25%,#15203f 100%);border-radius:100px 100px 0 0"></div>
<h2 class="abs qc-h">QUICK CONTACT</h2>
<p class="abs qc-sub">If you use this site regularly and would like to help keep the site on the Internet</p>
<div class="field" style="left:599px;top:2991px;width:250px;height:34px">Name:</div>
<div class="field" style="left:599px;top:3031px;width:250px;height:34px">Email:</div>
<div class="field" style="left:599px;top:3071px;width:250px;height:34px">Phone:</div>
<div class="field" style="left:599px;top:3111px;width:250px;height:34px">Practice Area:</div>
<div class="field" style="left:857px;top:2991px;width:250px;height:154px">Message:</div>
<div class="submit">SUBMIT</div>

<footer class="abs footer"></footer>
<h4 class="f-h" style="left:93px">Quick Links</h4>
<ul class="f-list" style="left:93px">
  <li><span class="dot"></span>Home</li>
  <li><span class="dot"></span>Family Law</li>
  <li><span class="dot"></span>Criminal Law</li>
  <li><span class="dot"></span>About</li>
  <li><span class="dot"></span>Contact</li>
</ul>
<h4 class="f-h" style="left:275px">Services</h4>
<ul class="f-list" style="left:275px">
  <li><span class="dot"></span>Family Law</li>
  <li><span class="dot"></span>Criminal Law</li>
</ul>
<h4 class="f-h" style="left:441px">Contact Us</h4>
<div class="f-contact">
  <div><svg width="10" height="12" viewBox="0 0 10 12"><path d="M5 0a4 4 0 0 1 4 4c0 3-4 8-4 8S1 7 1 4a4 4 0 0 1 4-4z" fill="#4a78e0"/><circle cx="5" cy="4" r="1.5" fill="#1c1c1d"/></svg><span>40 Meridian Plaza Drive Suite 405<br>Harborview, NJ 07000</span></div>
  <div><svg width="10" height="12" viewBox="0 0 10 12"><path d="M2 0h2l1 3-1.5 1a6 6 0 0 0 3 3L8 5.5l2 1v2c0 1-1 1.5-2 1.5C4 10 0 6 0 2 0 1 1 0 2 0z" fill="#4a78e0"/></svg><span>(555) 742-6093</span></div>
  <div><svg width="11" height="12" viewBox="0 0 11 12"><rect x="0" y="2" width="11" height="9" rx="1" fill="#4a78e0"/><rect x="2" y="0" width="7" height="4" fill="#4a78e0"/></svg><span>(555) 742-6018</span></div>
  <div><svg width="11" height="12" viewBox="0 0 11 12"><rect x="0" y="2" width="11" height="8" rx="1" fill="#4a78e0"/><path d="M0 3l5.5 4L11 3" fill="none" stroke="#1c1c1d" stroke-width="1"/></svg><span>info@tallowfinchlaw.com</span></div>
</div>
<h4 class="f-h" style="left:712px">Location</h4>
<div class="photo" role="img" aria-label="Street map showing the office location" style="left:713px;top:3349px;width:394px;height:149px;background:linear-gradient(135deg,#eef0ec 0%,#e3e7e1 60%,#d7e4f1 100%)"></div>
<div class="social f-social"><span></span><span></span><span></span></div>
<p class="copy">Copyright © 2020 <b>Tallow | Finch</b>. All rights reserved.</p>

</body>
</html>
```